Templates for ppt, word and a new, modern and fresh "look" for this...

We need some new templates for our product datasheet, manuals and powerpoint templates. We are a manufacturer and distributor of gas saving equipment for welding industry mainly.

```html
<!DOCTYPE html>
<html lang="en">
<head>
<meta charset="utf-8">
<title>Weldora document templates</title>
<link href="https://fonts.googleapis.com/css2?family=Carlito:wght@400;700&display=swap" rel="stylesheet">
<style>
:root{
  --navy:#273a7f;
  --red:#d8302f;
  --sky:#cfe9f5;
  --sky-line:#a9d4ea;
  --grey-bg:#cbcbcb;
  --ink:#2b2b2b;
  --muted:#7b7b7b;
  --rule:#d5d5d5;
  --paper:#ffffff;
}
*{box-sizing:border-box;margin:0;padding:0}
html,body{width:945px;height:1200px;overflow:hidden}
body{background:var(--grey-bg);font-family:"Carlito","Calibri",sans-serif;color:var(--ink);position:relative}
.page{position:absolute;width:248px;height:350px;background:var(--paper);box-shadow:3px 4px 8px rgba(0,0,0,.28);overflow:hidden}
.col-1{left:69px}.col-2{left:342px}.col-3{left:613px}
.row-1{top:58px}.row-2{top:429px}.row-3{top:806px}

.client-name{position:absolute;top:9px;right:20px;font-size:3.6px;letter-spacing:.1px;color:#444}
.page-title{position:absolute;left:22px;right:20px;top:22px;font-size:9.5px;color:var(--navy);padding-bottom:2px;border-bottom:.5px solid var(--rule);letter-spacing:.1px}
.content{position:absolute;left:22px;right:20px;top:42px;font-size:4.1px;line-height:7px}
.content p{margin-bottom:5px}
h3.section{font-size:7px;font-weight:400;color:#333;margin:4px 0 1px}
h4.sub{font-size:7.4px;font-weight:400;color:#333;margin:3px 0 2px}
.lede{color:var(--navy)}

.footer{position:absolute;left:22px;right:12px;bottom:11px;height:10px;display:flex;align-items:center}
.wordmark{font-weight:700;color:var(--navy);font-size:8px;letter-spacing:-.1px}
.footer .rule{flex:1;height:.8px;background:#9a9a9a;margin:0 6px 0 8px}
.page-no{width:9px;height:9px;border-radius:50%;background:var(--red);color:#fff;font-size:4.5px;display:flex;align-items:center;justify-content:center}

/* cover */
.cover svg{position:absolute;left:0;top:0}
.cover-title{position:absolute;left:55px;top:71px;color:#fff;font-size:11.4px;line-height:13px;letter-spacing:.1px}
.cover-sub{position:absolute;left:55px;top:107px;color:#8e9fcf;font-size:7.2px;line-height:10px}
.cover-mark{position:absolute;right:24px;top:292px;font-size:24px;font-weight:700;color:var(--navy);letter-spacing:-.3px}

/* toc */
.toc-head{font-size:7px;font-weight:700;color:#333;margin:3px 0 6px}
.toc li{list-style:none;display:flex;align-items:baseline;font-size:3.9px;height:8.3px;color:#222}
.toc li.l2{padding-left:5px}.toc li.l3{padding-left:8px}
.toc li.strong{font-weight:700}
.toc .dots{flex:1;border-bottom:.5px dotted #555;margin:0 6px;transform:translateY(-1px)}
.toc .num{width:8px;text-align:right}

/* exec summary */
.numbered{display:flex;gap:4px;align-items:baseline}
.numbered .n{width:6px;margin-left:-10px;font-size:5px;color:#555}
.em{font-style:italic;color:#555}
.indent{padding-left:10px}

/* vision */
.mission-band{display:flex;align-items:center;background:#8c8c8c;color:#fff;font-size:4.6px;line-height:5.6px;height:23px;margin:2px 0 7px}
.mission-band .icon{width:23px;height:23px;background:var(--navy);display:flex;align-items:center;justify-content:center;margin-right:9px;flex:none}
.center-note{text-align:center;color:var(--navy)}
.link{color:var(--navy);text-decoration:underline}

/* tables */
table.grid{width:100%;border-collapse:separate;border-spacing:2px 2.1px;font-size:3.9px;margin:-2px -2px 0;width:calc(100% + 4px)}
.grid th{background:#d6d6d6;font-weight:400;height:6.5px;padding:0 4px}
.grid td{background:var(--sky);height:6.5px;padding:0 5px}
.grid td.c{text-align:center}
.grid tr.phase td{color:var(--navy);font-size:4.4px}
.grid tr.total td{background:#dedede;font-weight:700}
.grid tr.grand td{background:var(--navy);color:#fff;font-size:4.4px;font-weight:700}
.grid.navy-head th{background:var(--navy);color:#fff}

/* needs */
.intro-grey{font-size:6px;line-height:6.4px;color:#8a8a8a}
.legend{display:grid;grid-template-columns:repeat(4,1fr);row-gap:6px;font-size:3.3px;color:#555;margin:10px 0 0 8px}
.legend span{display:flex;align-items:center;gap:2px}
.legend i{width:5px;height:5px;display:inline-block}

/* headline pages */
.photo{background:linear-gradient(135deg,#c7ccd0 0%,#8c98a6 45%,#3a4150 100%)}
.headline-blue{font-size:6.1px;line-height:6.5px;font-weight:700;color:var(--navy);margin:8px 0 5px}
.form-stripes{margin:6px 6px 8px}
.form-stripes div{height:7.5px;background:#dae8f6;border-top:.5px solid #8eb2d8;margin-bottom:7px}
.hl-blue{color:var(--navy)}

/* back */
.back-contact{position:absolute;left:46px;top:304px;display:flex;align-items:center;gap:5px}
.back-contact .wordmark{font-size:14px}
.back-contact .details{font-size:3.2px;line-height:4px;color:#333;border-left:.5px solid #999;padding-left:3px}
.back-contact .addr{font-size:3.2px;line-height:4px;color:var(--navy)}
</style>
</head>
<body>

<!-- Cover -->
<section class="page col-1 row-1 cover">
  <svg width="248" height="350" viewBox="0 0 248 350" aria-hidden="true">
    <polygon points="0,0 248,0 248,141 0,225" fill="var(--navy)"/>
    <polygon points="0,225 248,141 248,188 0,235" fill="var(--red)"/>
  </svg>
  <h1 class="cover-title">LOREM IPSUM IS SIMPLY<br>DUMMY HAS BEEN</h1>
  <p class="cover-sub">LOREM IPSUM IS SIMPLY ETIAM<br>VESTIBULUM</p>
  <div class="cover-mark">Weldora</div>
</section>

<!-- Table of contents -->
<section class="page col-2 row-1">
  <div class="client-name">THE CLIENT NAME</div>
  <h2 class="page-title">TABLE OF CONTENTS</h2>
  <div class="content" style="top:48px">
    <div class="toc-head">Contents</div>
    <ul class="toc">
      <li class="strong">1. Table of Contents<span class="dots"></span><span class="num">01</span></li>
      <li class="l2">1.1. Executive Summary<span class="dots"></span><span class="num">02</span></li>
      <li class="l3">1.1.1. Our Understanding of Your Needs<span class="dots"></span><span class="num">02</span></li>
      <li class="strong">2. Our Recommendations<span class="dots"></span><span class="num">03</span></li>
      <li class="l2">2.1. Our Approach<span class="dots"></span><span class="num">05</span></li>
      <li class="l3">2.1.1. Budget and Timeframe<span class="dots"></span><span class="num">07</span></li>
      <li>3. Appendix A: About Harlow Creek<span class="dots"></span><span class="num">10</span></li>
      <li class="l2">3.1. Appendix B: Selected Client List<span class="dots"></span><span class="num">10</span></li>
      <li class="l3">3.1.1. Appendix C: Our Capabilities<span class="dots"></span><span class="num">11</span></li>
      <li>Appendix D: Our Process<span class="dots"></span><span class="num">12</span></li>
    </ul>
  </div>
  <footer class="footer"><span class="wordmark">Weldora</span><span class="rule"></span><span class="page-no">1</span></footer>
</section>

<!-- Executive summary -->
<section class="page col-3 row-1">
  <div class="client-name">THE CLIENT NAME</div>
  <h2 class="page-title">EXECUTIVE SUMMARY</h2>
  <div class="content indent" style="top:44px;left:15px">
    <h3 class="section numbered"><span class="n">1</span>Solution</h3>
    <p><span class="em">AI automated accounting</span><br>Ledgerly builds automation in stages on top of its current system to reach full automation thanks to the Ledgerly AI. Ledgerly AI automates every manual task performed by the user. It starts by connecting to all sources of accounting data such as bank accounts, credit card, webshop or document management systems (FileBay or Vaultly). Based on these datas, Ledgerly AI creates bookings and generates financial reports. Finally, Ledgerly AI features chat-like interface that allows users to communicate seamlessly with it, viewing it as a trusted advisor over time for all their accounting queries.</p>
    <p><span class="em">Blockchain software license or Token-as-a-License (TaaL)</span><br>It is possible to create tokens on blockchain that represent software licenses, also known as Token-as-a-Licence (TaaL). Ledgerly creates TaaL by using the Meridian official wallet which interacts with the Meridian blockchain. Upon purchase of TaaL, the token holder is free to transfer or sell TaaL using secondary market that is built directly over the blockchain, in our case, the Meridian marketplace. Ledgerly checks the validity of a token against the blockchain ensuring that token holders have access to the software. TaaL make distribution and securisation of software licenses easier for software developers. It also makes the management and resale of software license easier for software owners. All in all, TaaL has a higher value as a normal software license.</p>
    <h3 class="section numbered"><span class="n">2.</span>Pre-ICO Token sale</h3>
    <p>To realize this innovative vision, Ledgerly is launching a pre-ICO in form of a token sale on Meridian blockchain. 20,000,000 tokens are available to purchase for the price of CHF 0.10 each during a 30-day period to be announced. Tokens represent Ledgerly lifelong software licenses and by purchasing enough tokens, holders gain access to Ledgerly software. 15,000 tokens give access to Ledgerly invoicing or accounting. 20,000 tokens give access to both Ledgerly accounting and invoicing. Future customers will still have the opportunity to buy directly yearly or monthly subscriptions to have access to Ledgerly.</p>
    <h3 class="section">Future plans</h3>
    <p>A future ICO is planned between 18 and 24 months after the pre-ICO token sale. This offering will support the development of Ledgerly into a fully decentralized, privacy-focused ecosystem of applications. The new model will reward each participant so that a new world with zero administrative tasks becomes reality.</p>
  </div>
  <footer class="footer"><span class="wordmark">Weldora</span><span class="rule"></span><span class="page-no">1</span></footer>
</section>

<!-- Vision -->
<section class="page col-1 row-2">
  <div class="client-name">THE CLIENT NAME</div>
  <h2 class="page-title" style="left:24px">VISION</h2>
  <div class="content" style="top:44px;font-size:4px;line-height:6.3px">
    <div class="mission-band">
      <div class="icon"><svg width="16" height="16" viewBox="0 0 16 16" aria-hidden="true"><circle cx="8" cy="8" r="7" fill="none" stroke="#fff" stroke-width="1.2"/><circle cx="8" cy="8" r="4.5" fill="none" stroke="#fff" stroke-width="1.2"/><circle cx="8" cy="8" r="2" fill="#fff"/><path d="M8 8 L14 2" stroke="#fff" stroke-width="1"/></svg></div>
      <div>Ledgerly's mission is to help and support the self-employed and small business owners with their administrative tasks so they can focus on what matters -- their business.</div>
    </div>
    <p>Administrative tasks are cumbersome, time-consuming and often prevent small owners from focusing their time and energy on their business and their customers. They can also be extremely stressful and nerve-wracking for those attempting these tasks for the first time.</p>
    <p class="center-note">At Ledgerly, we envisage accounting for the self-employed and small business owners as being automated and decentralized</p>
    <p>Accounting can and should be done automatically. By connecting to all sources of accounting data such as bank accounts, payment systems, e-commerce websites, and invoicing systems, Ledgerly AI automatically completes these tasks, which would take hours to do manually. Bookings are created automatically and fully completed. Financial statements are available within a couple of clicks, and after analysing your data, Ledgerly AI will offer you tips to improve your financial stability.</p>
    <p>What may seem like a pipedream to the millions of self-employed who struggle with their admin, is already a reality. Now is the time to join Ledgerly on its mission to transform the world of bookkeeping through the power of AI</p>
    <h4 class="sub">The Ledgerly model</h4>
    <p>Ledgerly is based on an innovative license model that uses Token-as-a-License (TaaL). The token represents lifelong software license for Ledgerly solutions. The Pre-ICO token sales will enable Ledgerly to complete its development of Ledgerly AI to deliver fully automatic bookkeeping.</p>
    <p>The Pre-ICO token sale will also pave the way for a future Ledgerly ICO. Ledgerly will launch accounting on the blockchain and ensure your accounting data is comprehensive and private, but available everywhere within your preferred apps. It will empower you to manage your data as you see fit in a fully decentralized way.<br>Furthermore, a new range of business apps will connect to Ledgerly to provide you</p>
    <p>with leading edge business data access to ensure you have the best available data at your fingertips.</p>
    <p>Ledgerly supports strong data ownership laws that truly protect individuals and ensure they have complete ownership of their data. Through decentralisation Ledgerly helps to ensure you always have full ownership of your data to decide how it should be used.</p>
    <p>To find out more about the Ledgerly AI project, and the Ledgerly TaaL or if you are interested in purchasing Ledgerly TaaL, please register with your email at <span class="link">https://www.ledgerly.example/ico</span> so we can notify you about our upcoming purchase periods.</p>
  </div>
  <footer class="footer"><span class="wordmark">Weldora</span><span class="rule"></span><span class="page-no">1</span></footer>
</section>

<!-- Budget and timeframe -->
<section class="page col-2 row-2">
  <div class="client-name">THE CLIENT NAME</div>
  <h2 class="page-title">BUDGET AND TIMEFRAME</h2>
  <div class="content" style="top:44px">
    <h4 class="sub" style="margin-top:0">Implementation Estimate</h4>
    <p>The bulk of the implementation costs will be defined by discovery. Based on similar CRM implementation projects, we feel expect that the CRM side will be somewhere between 200 and 300 hours, give or take. The wide swing in hours in phase one is related to the ill-defined nature of both the integration needs and our role in the integration project. Our focus in discovery (as mentioned above) will be to nail down those requirements and our role as it relates to what is needed to integrate the sites with the CRM.</p>
    <table class="grid">
      <tr><th style="width:52%">Task</th><th style="width:18%">Hours</th><th>Cost</th></tr>
      <tr><td>Discovery</td><td class="c">40</td><td class="c">$8,000</td></tr>
      <tr class="phase"><td colspan="3">Phase 1</td></tr>
      <tr><td>Discovery</td><td class="c">20-40</td><td class="c">$8,000</td></tr>
      <tr><td>Discovery</td><td class="c">20-40</td><td class="c">$8,000</td></tr>
      <tr><td>Discovery</td><td class="c">20-40</td><td class="c">$8,000</td></tr>
      <tr class="total"><td>Total Phase 1</td><td class="c">80-240</td><td class="c">$16,800-40,000</td></tr>
      <tr class="phase"><td colspan="3">Phase 2</td></tr>
      <tr><td>Discovery</td><td class="c">20-40</td><td class="c">$8,000</td></tr>
      <tr class="total"><td>Total Phase 2</td><td class="c">80-240</td><td class="c">$16,800-40,000</td></tr>
      <tr class="grand"><td>Total Estimated Implementation Cost</td><td class="c">220-480</td><td class="c">$44,000-96,000</td></tr>
    </table>
    <h4 class="sub" style="margin-top:10px">Project Timeline</h4>
    <p>Based on the information we have at our disposal, the March 21st launch date doesn't seem a realistic goal to get both the work done needed to provide the foundation for the future CRM instance and the integration given the state of apparent flux of the requirements. That said, we feel it prudent to proceed with discovery before committing to or pushing that date. We are currently estimating that the first phase will take somewhere between 7 and 12 weeks (including discovery) to complete.</p>
    <table class="grid navy-head" style="margin-top:6px">
      <tr><th style="width:63%">Task</th><th>Weeks to Complete</th></tr>
      <tr><td>Discovery</td><td class="c">1-2</td></tr>
      <tr><td>Phase 1</td><td class="c">6-10</td></tr>
      <tr><td>Phase 2</td><td class="c">8-12</td></tr>
      <tr class="total"><td>Total Number of Weeks</td><td></td></tr>
    </table>
  </div>
  <footer class="footer"><span class="wordmark">Weldora</span><span class="rule"></span><span class="page-no">1</span></footer>
</section>

<!-- Understanding of needs -->
<section class="page col-3 row-2">
  <div class="client-name">THE CLIENT NAME</div>
  <h2 class="page-title">OUR UNDERSTANDING OF YOUR NEEDS</h2>
  <div class="content" style="top:42px">
    <p class="intro-grey">Ledgerly's mission is to help and support the self-employed and small business owners with</p>
    <svg width="206" height="118" viewBox="0 0 206 118" role="img" aria-label="Pie chart of share by country">
      <ellipse cx="117" cy="66" rx="38" ry="36" fill="#4b5aa8"/>
      <g transform="translate(117 62) scale(1 .95) rotate(-90)">
        <circle r="18" fill="none" stroke-width="36" stroke="#73bde3" stroke-dasharray="34.50 113.1" stroke-dashoffset="0"/>
        <circle r="18" fill="none" stroke-width="36" stroke="#6189cc" stroke-dasharray="20.70 113.1" stroke-dashoffset="-34.50"/>
        <circle r="18" fill="none" stroke-width="36" stroke="#5c6bc0" stroke-dasharray="13.80 113.1" stroke-dashoffset="-55.20"/>
        <circle r="18" fill="none" stroke-width="36" stroke="#6c60ba" stroke-dasharray="11.42 113.1" stroke-dashoffset="-69.00"/>
        <circle r="18" fill="none" stroke-width="36" stroke="#8a6abc" stroke-dasharray="9.61 113.1" stroke-dashoffset="-80.42"/>
        <circle r="18" fill="none" stroke-width="36" stroke="#9d6cc2" stroke-dasharray="8.82 113.1" stroke-dashoffset="-90.03"/>
        <circle r="18" fill="none" stroke-width="36" stroke="#b56cba" stroke-dasharray="6.79 113.1" stroke-dashoffset="-98.85"/>
        <circle r="18" fill="none" stroke-width="36" stroke="#c96eaa" stroke-dasharray="4.07 113.1" stroke-dashoffset="-105.64"/>
        <circle r="18" fill="none" stroke-width="36" stroke="#dc6c8a" stroke-dasharray="3.39 113.1" stroke-dashoffset="-109.71"/>
      </g>
      <g font-size="3.3" fill="#555" font-family="Carlito, sans-serif">
        <text x="18" y="34">The Netherlands: 3.0%</text>
        <text x="39" y="41">Belgium: 3.6%</text>
        <text x="45" y="48">UK: 6.0%</text>
        <text x="41" y="55">Austria: 7.8%</text>
        <text x="39" y="62">Australia: 8.5%</text>
        <text x="28" y="78">Germany: 10.1%</text>
        <text x="31" y="92">Ireland: 12.2%</text>
        <text x="162" y="52">Lithuania: 30.5%</text>
        <text x="161" y="86">Czech Republic: 18.3%</text>
      </g>
    </svg>
    <div class="legend">
      <span><i style="background:#73bde3"></i>Lithuania 30.5%</span>
      <span><i style="background:#6189cc"></i>Czech Republic 18.3%</span>
      <span><i style="background:#5c6bc0"></i>Ireland 12.2%</span>
      <span><i style="background:#6c60ba"></i>Germany 10.1%</span>
      <span><i style="background:#8a6abc"></i>Australia 8.5%</span>
      <span><i style="background:#9d6cc2"></i>Austria 7.8%</span>
      <span><i style="background:#b56cba"></i>UK 6.0%</span>
      <span><i style="background:#c96eaa"></i>Belgium 3.6%</span>
      <span><i style="background:#dc6c8a"></i>The Netherlands 3.0%</span>
    </div>
    <h4 class="sub" style="margin-top:20px;margin-bottom:0">Lorem Ipsum</h4>
    <p>The bulk of the implementation costs will be defined by discovery. Based on similar CRM implementation projects, we feel expect that the CRM side will be somewhere between 200 and 300 hours, give or take. The wide swing in hours in phase one is related to the ill-defined nature of both the integration needs and our role in the integration project. Our focus in discovery (as mentioned above) will be to nail down those requirements and our role as it relates to what is needed to integrate the sites with the CRM.</p>
    <p>The bulk of the implementation costs will be defined by discovery. Based on similar CRM implementation projects, we feel expect that the CRM side will be somewhere between 200 and 300 hours, give or take. The wide swing in hours in phase one is related to the ill-defined nature of both the integration needs and our role in the integration project. Our focus in discovery (as mentioned above) will be to nail down those requirements and our role as it relates to what is needed to integrate the sites with the CRM.</p>
  </div>
  <footer class="footer"><span class="wordmark">Weldora</span><span class="rule"></span><span class="page-no">1</span></footer>
</section>

<!-- Headline page A -->
<section class="page col-1 row-3">
  <div class="client-name">THE CLIENT NAME</div>
  <h2 class="page-title">HEADLINE HERE</h2>
  <div class="content" style="top:43px;font-size:4px;line-height:6.3px">
    <div class="photo" role="img" aria-label="Photo of a businessman drawing a cloud network diagram with arrows" style="height:89px;margin-right:3px"></div>
    <p class="headline-blue">Ledgerly's mission is to help and support the self-employed and small business owners with</p>
    <p>Administrative tasks are cumbersome, time-consuming and often prevent small owners from focusing their time and energy on their business and their customers. They can also be extremely stressful and nerve-wracking for those attempting these tasks for the first time.</p>
    <p>At Ledgerly, we envisage accounting for the self-employed and small business owners as being <span class="hl-blue">automated and decentralized</span></p>
    <div class="form-stripes"><div></div><div></div><div></div><div></div></div>
    <p>Ledgerly is based on an innovative license model that uses Token-as-a-License (TaaL). The token represents lifelong software license for Ledgerly solutions. The Pre-ICO token sales will enable Ledgerly to complete its development of Ledgerly AI to deliver fully automatic bookkeeping.</p>
    <p>with leading edge business data access to ensure you have the best available data at your fingertips.</p>
  </div>
  <footer class="footer"><span class="wordmark">Weldora</span><span class="rule"></span><span class="page-no">1</span></footer>
</section>

<!-- Headline page B -->
<section class="page col-2 row-3">
  <div class="client-name">THE CLIENT NAME</div>
  <h2 class="page-title">HEADLINE HERE</h2>
  <div class="photo" role="img" aria-label="Photo of a hand drawing arrows on a chalk diagram" style="position:absolute;left:22px;top:44px;width:87px;height:131px"></div>
  <div class="photo" role="img" aria-label="Photo of a businessman in a suit beside a drawn cloud" style="position:absolute;left:22px;top:197px;width:87px;height:115px"></div>
  <div class="content" style="left:124px;top:43px;font-size:4px;line-height:6.2px">
    <p class="headline-blue" style="font-size:6.6px;line-height:6.7px;margin-top:0">Ledgerly's mission is to help and support the self-employed and small business owners with their administrative tasks so they can focus on what matters -- their business.</p>
    <p>Administrative tasks are cumbersome, time-consuming and often prevent small owners from focusing their time and energy on their business and their customers. They can also be extremely stressful and nerve-wracking for those attempting these tasks for the first time.</p>
    <p>At Ledgerly, we envisage accounting for the self-employed and small business owners as being <span class="hl-blue">automated and decentralized</span></p>
    <p>Accounting can and should be done automatically. By connecting to all sources of accounting data such as bank accounts, payment systems, e-commerce websites, and invoicing systems, Ledgerly AI automatically completes these tasks, which would take hours to do manually. Bookings are created automatically and fully completed. Financial statements are available within a couple of clicks, and after analysing your data, Ledgerly AI will offer you tips to improve your financial stability.</p>
    <p>What may seem like a pipedream to the millions of self-employed who struggle with</p>
    <h4 class="sub">The Ledgerly model</h4>
    <p>Ledgerly is based on an innovative license model that uses Token-as-a-License (TaaL). The token represents lifelong software license for Ledgerly solutions. The Pre-ICO token sales will enable Ledgerly to complete its development of Ledgerly AI to deliver fully automatic</p>
  </div>
  <footer class="footer"><span class="wordmark">Weldora</span><span class="rule"></span><span class="page-no">1</span></footer>
</section>

<!-- Back cover -->
<section class="page col-3 row-3 cover">
  <svg width="248" height="350" viewBox="0 0 248 350" aria-hidden="true">
    <polygon points="0,0 248,0 248,189 0,291" fill="var(--navy)"/>
    <polygon points="0,291 248,189 248,236 0,300" fill="var(--red)"/>
  </svg>
  <div class="back-contact">
    <span class="wordmark">Weldora</span>
    <div class="details">P: 000-555-0142 Ext 200<br>E: hello@weldora.example<br>W: www.weldora.example</div>
    <div class="addr">12 Foundry Lane, Suite 4<br>Northgate Province AB 0000</div>
  </div>
</section>

</body>
</html>
```